Physiotherapiepraxis braucht Druckvorlage für Werbeanzeige
Zielgruppe
Dienstleistung im Gesundheitswesen als Physiotherapiepraxis.
Krankengymnastik, auch im häuslichen Bereich oder im Altersheim, und Massage sowie Wellnessanwendungen.
Zielgruppe sind primär Erwachsene, eingeschränkt auch Kinder.
Aufgabenstellung
Ich möchte eine Druckvorlage für eine Werbeanzeige, die ich immer mal wieder in verschiedenen Festschriften im dörflichen Bereich oder in einer regionalen Zeitschrift veröffentlichen kann.
Die Anzeige soll das Logo enthalten und die Anschrift der Praxis sowie die Telefonnummer und Adresse der Homepage.

```html
<!DOCTYPE html>
<html lang="de">
<head>
<meta charset="utf-8">
<title>Anzeigen Physiotherapie Marlene Vossberg</title>
<link rel="stylesheet" href="https://fonts.googleapis.com/css2?family=PT+Sans:wght@400;700&display=swap">
<style>
  :root {
    --gold: #d3b823;
    --green: #007b3a;
    --charcoal: #555555;
    --silver: #b2b2b2;
    --label: #6e6e6e;
    --white: #ffffff;
  }
  * { box-sizing: border-box; margin: 0; padding: 0; }
  html, body { width: 1200px; height: 846px; overflow: hidden; background: var(--white); }
  body { position: relative; font-family: "PT Sans", Arial, sans-serif; }

  .section-label {
    position: absolute;
    font-size: 22px;
    color: var(--label);
    font-weight: 400;
  }

  .ad { position: absolute; border: 1px solid var(--frame); background: var(--white); }
  .ad--single { width: 257px; height: 258px; }
  .ad--double { width: 514px; height: 114px; display: flex; }

  .ad--gold { --frame: var(--gold); --info: var(--gold); --name: var(--green); --band: var(--gold); }
  .ad--green { --frame: var(--green); --info: var(--green); --name: var(--green); --band: var(--gold); }
  .ad--green-wide { --frame: var(--gold); --info: var(--green); --name: var(--green); --band: var(--gold); }
  .ad--grey { --frame: var(--charcoal); --info: var(--charcoal); --name: var(--charcoal); --band: var(--silver); }

  .brand { position: relative; height: 120px; }
  .ad--double .brand { width: 256px; height: 112px; flex: none; }

  .brand-name {
    position: absolute;
    left: 0; right: 0; top: 28px;
    display: flex; align-items: center; justify-content: center; gap: 8px;
    font-size: 19px;
    letter-spacing: 1.6px;
    color: var(--name);
    white-space: nowrap;
  }
  .brand-dot { width: 10px; height: 10px; border-radius: 50%; background: var(--name); flex: none; }

  .brand-band {
    position: absolute;
    left: 15px; top: 68px;
    width: 227px; height: 33px;
    background: var(--band);
    color: var(--white);
    font-size: 21px;
    letter-spacing: 0.3px;
    display: flex; align-items: center; justify-content: center;
  }

  .info {
    background: var(--info);
    color: var(--white);
    font-size: 14.5px;
    line-height: 18px;
  }
  .ad--single .info { height: 136px; padding: 7px 15px 0; }
  .ad--double .info { flex: 1; padding: 10px 12px 0; line-height: 19.5px; }
  .info strong { font-weight: 700; display: block; }
  .info span { display: block; }
  .info .gap { margin-top: 4px; }
  .ad--double .info .gap { margin-top: 0; }
</style>
</head>
<body>

<h2 class="section-label" style="left:143px; top:40px;">Anzeigen 1-spaltig, 45 mm breit</h2>

<article class="ad ad--single ad--gold" style="left:142px; top:81px;">
  <div class="brand">
    <div class="brand-name"><span class="brand-dot"></span>Marlene Vossberg</div>
    <div class="brand-band">PHYSIOTHERAPIE</div>
  </div>
  <div class="info">
    <strong>Praxis für Physiotherapie</strong>
    <strong>Marlene Vossberg</strong>
    <span class="gap">Lindenweg 7</span>
    <span>21499 Heidkamp</span>
    <span class="gap">Tel. 04158 473021</span>
    <strong>www.physiotherapie-heidkamp.de</strong>
  </div>
</article>

<article class="ad ad--single ad--green" style="left:471px; top:81px;">
  <div class="brand">
    <div class="brand-name"><span class="brand-dot"></span>Marlene Vossberg</div>
    <div class="brand-band">PHYSIOTHERAPIE</div>
  </div>
  <div class="info">
    <strong>Praxis für Physiotherapie</strong>
    <strong>Marlene Vossberg</strong>
    <span class="gap">Lindenweg 7</span>
    <span>21499 Heidkamp</span>
    <span class="gap">Tel. 04158 473021</span>
    <strong>www.physiotherapie-heidkamp.de</strong>
  </div>
</article>

<article class="ad ad--single ad--grey" style="left:800px; top:81px;">
  <div class="brand">
    <div class="brand-name"><span class="brand-dot"></span>Marlene Vossberg</div>
    <div class="brand-band">PHYSIOTHERAPIE</div>
  </div>
  <div class="info">
    <strong>Praxis für Physiotherapie</strong>
    <strong>Marlene Vossberg</strong>
    <span class="gap">Lindenweg 7</span>
    <span>21499 Heidkamp</span>
    <span class="gap">Tel. 04158 473021</span>
    <strong>www.physiotherapie-heidkamp.de</strong>
  </div>
</article>

<h2 class="section-label" style="left:343px; top:383px;">Anzeigen 2-spaltig, 90 mm breit</h2>

<article class="ad ad--double ad--gold" style="left:343px; top:422px;">
  <div class="brand">
    <div class="brand-name"><span class="brand-dot"></span>Marlene Vossberg</div>
    <div class="brand-band">PHYSIOTHERAPIE</div>
  </div>
  <div class="info">
    <strong>Praxis für Physiotherapie</strong>
    <strong>Marlene Vossberg</strong>
    <span class="gap">Lindenweg 7, 21499 Heidkamp</span>
    <span>Tel. 04158 473021</span>
    <strong>www.physiotherapie-heidkamp.de</strong>
  </div>
</article>

<article class="ad ad--double ad--green-wide" style="left:343px; top:557px;">
  <div class="brand">
    <div class="brand-name"><span class="brand-dot"></span>Marlene Vossberg</div>
    <div class="brand-band">PHYSIOTHERAPIE</div>
  </div>
  <div class="info">
    <strong>Praxis für Physiotherapie</strong>
    <strong>Marlene Vossberg</strong>
    <span class="gap">Lindenweg 7, 21499 Heidkamp</span>
    <span>Tel. 04158 473021</span>
    <strong>www.physiotherapie-heidkamp.de</strong>
  </div>
</article>

<article class="ad ad--double ad--grey" style="left:343px; top:693px;">
  <div class="brand">
    <div class="brand-name"><span class="brand-dot"></span>Marlene Vossberg</div>
    <div class="brand-band">PHYSIOTHERAPIE</div>
  </div>
  <div class="info">
    <strong>Praxis für Physiotherapie</strong>
    <strong>Marlene Vossberg</strong>
    <span class="gap">Lindenweg 7, 21499 Heidkamp</span>
    <span>Tel. 04158 473021</span>
    <strong>www.physiotherapie-heidkamp.de</strong>
  </div>
</article>

</body>
</html>
```